hostels chain website in Barcelona

We need a web design for a brand of youth hostels located in Barcelona called El Patio Mirasol. We have two hostels with different location. We offer cheap accomodation in shared dorms for young people (avg. 23 years old), but we aim to arrive to cultural tourist more than party people. We offer a local experience by hiring only local staff and by doing some free activities related to Barcelona.
Updates

Hello, In our website it has to appear the number and logo of the official agency that approve the bussiness. It is in our website, it is an orange box with the number 341 and 729. Besides this, we also like to have the wanderlogue box where it is possible to read reviews. Regards Marisol

Target Market(s)

Young people between 18 to 35 years old, that loves travelling and living new experiences.

Industry/Entity Type

Tourist

Other font styles liked:
• Gladifilthefte and Rockwell

Requirements
Must have
• Pictures of the hostel, booking buttom, groups section and activities section.
It must talk about two different locations.
Colors and design has to be related to the decoration of the hostel and the logo.
Nice to have
• It has to show happiness and cleanliness. we like the website http://www.patiolunahost.com/ as a reference.
Should not have
• Boring things

```html
<!DOCTYPE html>
<html lang="en">
<head>
<meta charset="utf-8">
<title>El Patio Mirasol – Barcelona Hostels</title>
<link href="https://fonts.googleapis.com/css2?family=Arimo&family=Neucha&family=Amatic+SC:wght@700&family=Pirata+One&family=Open+Sans:wght@400;700&display=swap" rel="stylesheet">
<style>
:root{
  --ink:#222;
  --grey:#777;
  --muted:#8a8a8a;
  --teal:#0f938a;
  --teal-dark:#0c7c74;
  --panel:#403f3d;
  --line:#bdbdbd;
  --photo-a:#cfe0ee;
  --photo-b:#b7a592;
  --white:#fff;
}
*{box-sizing:border-box;margin:0;padding:0}
html,body{width:1200px;height:1150px;overflow:hidden;background:var(--white)}
body{position:relative;font-family:'Arimo',Arial,sans-serif;color:var(--ink)}
.abs{position:absolute}

.brand{left:100px;top:22px;width:140px;font-family:'Neucha',cursive;font-size:30px;line-height:30px;color:var(--ink)}
.brand-dot{left:206px;top:8px;width:16px;height:16px;border-radius:50%;background:var(--ink)}

.like{left:781px;top:40px;display:flex;align-items:center;gap:6px;font-size:11px;font-family:Arial,sans-serif}
.like-btn{background:#4a66a0;color:#fff;font-weight:bold;font-size:11px;padding:3px 6px;border-radius:2px}

.langs{left:780px;top:80px;width:330px;font-family:'Open Sans',sans-serif;font-size:10px;letter-spacing:.8px;color:var(--muted);line-height:21px}
.langs span{margin-right:9px}
.langs i{font-style:normal;margin-right:9px}

.nav{left:100px;top:132px;width:998px;height:34px;border-top:1px dashed var(--line);border-bottom:1px dashed var(--line);display:flex;justify-content:space-between;align-items:center;padding:0 18px 0 4px;font-family:'Pirata One',cursive;font-size:17px;letter-spacing:1.5px;color:var(--ink)}

.hero{left:100px;top:185px;width:1000px;height:434px;border:1px solid #ccc;background:linear-gradient(180deg,var(--photo-a) 0%,#e8eef2 45%,var(--photo-b) 100%)}

.tile{top:636px;width:324px;height:113px;border:1px solid #ddd;display:flex;align-items:center;justify-content:center;font-family:'Neucha',cursive;font-size:72px;color:#333}
.tile.book{background:var(--teal);border-color:var(--teal-dark);color:var(--white);font-family:'Amatic SC',cursive;font-size:80px;letter-spacing:1px}

.booking{left:101px;top:795px;width:210px;height:244px;background:var(--panel);padding:2px 5px;font-family:'Open Sans',sans-serif;color:#ddd}
.booking label{display:block;font-size:11px;font-weight:bold;letter-spacing:.6px;margin-top:6px;line-height:14px}
.booking label:first-child{margin-top:0}
.row{display:flex;align-items:center;gap:5px;height:20px}
.select{background:#fff;border:1px solid #a9b7c9;height:17px;font-size:11px;color:#000;padding-left:4px;display:flex;align-items:center;justify-content:space-between}
.select b{width:14px;height:13px;margin-right:1px;background:#d7e2f4;border:1px solid #98a8c6;position:relative}
.select b::after{content:"";position:absolute;left:3px;top:4px;border:3px solid transparent;border-top:4px solid #345}
.day{font-size:12px;color:#ccc;font-family:Arial,sans-serif}
.nights{font-size:12px;color:#fff;font-weight:bold;padding-left:10px;gap:8px}
.pm{width:15px;height:14px;background:#fff;border-radius:3px;color:#333;font-size:12px;line-height:13px;text-align:center;font-weight:bold}
.check{margin-top:10px;height:28px;background:var(--teal);color:#fff;font-size:12px;font-weight:bold;display:flex;align-items:center;justify-content:center;letter-spacing:.3px}

.intro{left:377px;top:784px;width:725px}
.intro h1{font-family:'Neucha',cursive;font-weight:400;font-size:54px;color:#555;line-height:64px}
.intro p{margin-top:2px;font-size:15px;line-height:24px;color:var(--grey)}

.footer{left:100px;top:1074px;width:1000px;border-top:1px dashed var(--line);padding-top:12px;font-family:Arial,sans-serif;font-size:13px;color:var(--ink);display:flex}
.footer a{color:inherit;text-decoration:none;margin-left:4px}
.footer .copy{margin-left:auto;margin-right:3px}
</style>
</head>
<body>

<div class="abs brand">El Patio<br>Mirasol</div>
<div class="abs brand-dot"></div>

<div class="abs like"><span class="like-btn">Like</span><span>5,752 people like this.</span></div>

<div class="abs langs">
  <span>ENGLISH</span><i>|</i><span>FRANÇAIS</span><i>|</i><span>PORTUGUÊS</span><i>|</i><span>BRASILEIRO</span><i>|</i><br>
  <span>ITALIANO</span><i>|</i><span>ESPAÑOL</span><i>|</i><span>NEDERLANDSE</span><i>|</i>
</div>

<nav class="abs nav">
  <span>Home</span><span>The Hostel</span><span>Events</span><span>Contact</span><span>GALLERY</span><span>FAQ'S</span>
</nav>

<div class="abs hero" role="img" aria-label="Photo of a group of happy young travellers blowing bubbles in front of a Ferris wheel"></div>

<div class="abs tile" style="left:101px">Activities</div>
<div class="abs tile" style="left:439px">Groups</div>
<div class="abs tile book" style="left:777px">BOOK NOW !</div>

<form class="abs booking">
  <label>Hostel</label>
  <div class="row"><div class="select" style="width:194px">Mirasol Hostel Sun Terrace<b></b></div></div>
  <label>Arrival</label>
  <div class="row">
    <div class="select" style="width:49px">28<b></b></div>
    <div class="select" style="width:95px">Aug 2014<b></b></div>
    <span class="day">Thu</span>
    <svg width="21" height="19" viewBox="0 0 21 19"><rect x=".5" y=".5" width="20" height="18" fill="#fff" stroke="#bbb"/><rect x=".5" y=".5" width="20" height="5" fill="#d64a3a"/><path d="M1 9h19M1 13h19M6 6v12M11 6v12M16 6v12" stroke="#d88" stroke-width=".8"/></svg>
  </div>
  <label>Departure</label>
  <div class="row">
    <div class="select" style="width:49px">29<b></b></div>
    <div class="select" style="width:95px">Aug 2014<b></b></div>
    <span class="day">Fri</span>
    <svg width="21" height="19" viewBox="0 0 21 19"><rect x=".5" y=".5" width="20" height="18" fill="#fff" stroke="#bbb"/><rect x=".5" y=".5" width="20" height="5" fill="#d64a3a"/><path d="M1 9h19M1 13h19M6 6v12M11 6v12M16 6v12" stroke="#d88" stroke-width=".8"/></svg>
  </div>
  <label>Nights</label>
  <div class="row nights"><span>1</span><span class="pm">+</span><span class="pm">−</span></div>
  <label>Number of Guests:</label>
  <div class="row"><div class="select" style="width:34px">1<b></b></div></div>
  <div class="check">Check Availability</div>
</form>

<section class="abs intro">
  <h1>2 Barcelona Hostels</h1>
  <p>Sed ut perspiciatis unde omnis iste natus error sit voluptatem accusantium doloremque laudantium, totam rem aperiam, eaque ipsa quae ab illo inventore veritatis et quasi architecto beatae vitae dicta sunt explicabo. Nemo enim ipsam voluptatem quia voluptas sit aspernatur aut odit aut fugit, sed quia consequuntur magni dolores eos qui ratione voluptatem sequi nesciunt. Neque porro quisquam est, qui dolorem ipsum quia dolor sit amet, consectetur, adipisci velit, sed quia non numquam eius modi tempora incidunt ut labore et dolore magnam aliquam quaerat voluptatem. Ut enim ad minima veniam, quis nostrum exercitationem ullam corporis suscipit laboriosam, nisi ut aliquid ex ea commodi consequatur</p>
</section>

<footer class="abs footer">
  <a style="width:94px">Home</a>
  <a style="width:122px">The Hostel</a>
  <a style="width:95px">Events</a>
  <a style="width:101px">Contact</a>
  <a style="width:116px">GALLERY</a>
  <a>FAQ'S</a>
  <span class="copy">Copyright 2014</span>
</footer>

</body>
</html>
```